Business Card for Orvane Parts Wholesale supplier

Hi There! I need a new business card for our company. We are specialized in selling Orvane parts, mostly we sell new LCD screens for Telvox and Slatrons. I would like to see that back in the design.

You can find the colors and logo's on our website: www.dorvak-example.nl

Industry/Entity Type

Business

Contact Information for Business Card

My Details:
Lars Vintorp

Phone: 0031612873406
E-mail: Lars@dorvak-example.nl

Slogan: "Because Quality Matters"

Font styles to use
Sans Serif

Colors

Designer to choose colors to be used in the design.

Requirements
Must have
• A Black backside with the Dorvak logo on it. The front side should be clean with only my contact details.
• But I'm also open for something really different or awesome!
Nice to have
• Remember that we are in the parts & repairing industry, So i'll be handing those business cards mainly to repair companies. Maybe you can do something with that thought :)

```html
<!DOCTYPE html>
<html lang="en">
<head>
<meta charset="utf-8">
<title>Dorvak Business Card</title>
<link rel="stylesheet" href="https://fonts.googleapis.com/css2?family=Ubuntu:ital,wght@0,400;0,500;0,700;1,400&display=swap">
<style>
  :root {
    --stage: #2b2b2d;
    --card-white: #ffffff;
    --card-black: #0d0d0e;
    --card-black-soft: #202022;
    --orange: #f07a2a;
    --orange-light: #f49a55;
    --ink: #1b1b1b;
    --ink-muted: #6d6d6d;
    --white: #ffffff;
  }
  * { box-sizing: border-box; margin: 0; padding: 0; }
  html, body {
    width: 1200px;
    height: 950px;
    overflow: hidden;
    background: var(--stage);
    font-family: "Ubuntu", sans-serif;
  }
  .sheet {
    width: 1200px;
    height: 950px;
    display: flex;
    flex-direction: column;
    align-items: center;
    justify-content: center;
    gap: 60px;
  }
  .card {
    position: relative;
    width: 640px;
    height: 366px;
    overflow: hidden;
    box-shadow: 0 10px 30px rgba(0,0,0,0.45);
  }

  /* Front */
  .card-front { background: var(--card-white); }
  .front-accent {
    position: absolute;
    left: 0; top: 0;
    width: 40px; height: 100%;
    background: linear-gradient(180deg, var(--orange-light), var(--orange));
  }
  .wordmark {
    display: flex;
    align-items: center;
    gap: 10px;
    font-weight: 700;
    letter-spacing: 0.5px;
  }
  .wordmark-dot {
    border-radius: 50%;
    background: var(--orange);
    flex: none;
  }
  .front-wordmark {
    position: absolute;
    right: 40px; top: 36px;
    font-size: 34px;
    color: var(--ink);
  }
  .front-wordmark .wordmark-dot { width: 26px; height: 26px; }
  .contact {
    position: absolute;
    left: 96px; top: 170px;
  }
  .contact-name {
    font-size: 28px;
    font-weight: 700;
    color: var(--orange);
    margin-bottom: 14px;
  }
  .contact-line {
    font-size: 15px;
    color: var(--ink-muted);
    line-height: 1.7;
  }
  .contact-line .label { display: inline-block; width: 26px; }

  /* Back */
  .card-back {
    background: linear-gradient(135deg, var(--card-black-soft) 0%, var(--card-black) 55%);
    display: flex;
    flex-direction: column;
    align-items: center;
    justify-content: center;
    gap: 18px;
  }
  .back-wordmark {
    font-size: 58px;
    color: var(--white);
  }
  .back-wordmark .wordmark-dot { width: 40px; height: 40px; }
  .slogan {
    font-size: 17px;
    font-style: italic;
    color: var(--orange);
    letter-spacing: 0.5px;
  }
</style>
</head>
<body>
  <main class="sheet">
    <section class="card card-front" aria-label="Business card front">
      <div class="front-accent"></div>
      <div class="wordmark front-wordmark">
        <span class="wordmark-dot"></span>
        <span>Dorvak</span>
      </div>
      <div class="contact">
        <p class="contact-name">Lars Vintorp</p>
        <p class="contact-line"><span class="label">P :</span>0031612873406</p>
        <p class="contact-line"><span class="label">E :</span>Lars@dorvak-example.nl</p>
        <p class="contact-line"><span class="label">W :</span>www.dorvak-example.nl</p>
      </div>
    </section>

    <section class="card card-back" aria-label="Business card back">
      <div class="wordmark back-wordmark">
        <span class="wordmark-dot"></span>
        <span>Dorvak</span>
      </div>
      <p class="slogan">Because Quality Matters</p>
    </section>
  </main>
</body>
</html>
```